Contemporary Elegant Business Card Design for an International Trade Company in the Wine Industry

We need a new business card design for an international trade company in the wine and winemaking industry. The overall feel of the card should be contemporary, upscale, luxurious and elegant. It should communicate confidence and professionalism. The colors should complementary to our logo design (burgundy, gold, and black).
Inspiration: rich velvet tapestry
The card should include the following information:
Business: Corvelle Trading/Shipping, LLC.
Name: Martin R. Obrastow
Title: CEO
Email: marty@corvelletrading.example
Phone: 555-482-1957
www.corvelletrading.example
Reason: We'd like the designers that we requested some additional designs from to still submit designs. Thank you!
Business
Contact Information for Business Card
Title: CEO
Phone: 555-482-1957
www.corvelletrading.example

```html
<!DOCTYPE html>
<html lang="en">
<head>
<meta charset="utf-8">
<title>Corvelle Trading/Shipping – Business Card</title>
<link rel="stylesheet" href="https://fonts.googleapis.com/css2?family=Open+Sans:wght@400;600;700&display=swap">
<style>
  :root {
    --page-bg: #ece8e3;
    --card-burgundy: #4a1220;
    --card-burgundy-deep: #3a0d18;
    --card-black: #120c0d;
    --band-ivory: #fbf8f2;
    --accent-gold: #c9a24a;
    --text-light: #f4efe4;
    --text-dark: #1c1416;
    --text-muted: #5a4a4d;
  }
  * { box-sizing: border-box; margin: 0; padding: 0; }
  html, body { width: 1200px; height: 1000px; overflow: hidden; }
  body {
    background: var(--page-bg);
    font-family: "Open Sans", sans-serif;
    display: flex;
    flex-direction: column;
    align-items: center;
    justify-content: center;
    gap: 60px;
  }
  .card {
    width: 740px;
    height: 422px;
    position: relative;
    overflow: hidden;
    box-shadow: 0 10px 30px rgba(0,0,0,0.18);
  }

  /* Front */
  .card-front { background: var(--card-burgundy); }
  .top-strip {
    position: absolute; left: 0; top: 0; right: 0; height: 34px;
    background: var(--card-black);
  }
  .name-band {
    position: absolute; left: 0; top: 34px; right: 0; height: 104px;
    background: var(--band-ivory);
    border-bottom: 2px solid var(--accent-gold);
    box-shadow: 0 4px 10px rgba(0,0,0,0.3);
    z-index: 2;
  }
  .holder {
    position: absolute; left: 300px; top: 30px; width: 300px;
    text-align: center;
  }
  .holder-name { font-size: 26px; font-weight: 700; color: var(--text-dark); line-height: 1.2; }
  .holder-title { font-size: 15px; color: var(--text-muted); line-height: 1.3; }

  .brand-block {
    position: absolute; right: 0; top: 138px; bottom: 0; width: 430px;
    background: var(--card-black);
    clip-path: polygon(70px 0, 100% 0, 100% 100%, 0 100%);
  }
  .contact-list {
    position: absolute; left: 44px; top: 168px;
    list-style: none;
    display: flex; flex-direction: column; gap: 10px;
  }
  .contact-item {
    display: flex; align-items: center; gap: 16px;
    color: var(--text-light); font-size: 16px;
  }
  .contact-icon {
    width: 18px; height: 18px; background: var(--accent-gold);
    display: flex; align-items: center; justify-content: center;
    flex: none;
  }
  .contact-icon svg { width: 12px; height: 12px; }

  .brand { position: absolute; text-align: center; color: var(--text-light); }
  .card-front .brand { right: 40px; top: 240px; width: 320px; }
  .brand-name {
    display: inline-flex; align-items: center; gap: 12px;
    font-weight: 400; letter-spacing: 5px; color: var(--text-light);
  }
  .brand-mark { width: 22px; height: 22px; background: var(--accent-gold); display: inline-block; }
  .card-front .brand-name { font-size: 28px; }
  .company { font-size: 18px; margin-top: 8px; color: var(--text-light); }

  /* Back */
  .card-back { background: var(--card-burgundy-deep); }
  .card-back .brand { left: 0; right: 0; top: 130px; }
  .card-back .brand-name { font-size: 40px; }
  .card-back .brand-mark { width: 30px; height: 30px; }
  .card-back .company { font-size: 26px; font-weight: 700; margin-top: 14px; }
  .website { font-size: 14px; margin-top: 8px; color: var(--accent-gold); }
</style>
</head>
<body>
  <section class="card card-front" aria-label="Business card front">
    <div class="top-strip"></div>
    <div class="name-band">
      <div class="holder">
        <p class="holder-name">Martin R. Obrastow</p>
        <p class="holder-title">CEO</p>
      </div>
    </div>
    <div class="brand-block"></div>
    <ul class="contact-list">
      <li class="contact-item">
        <span class="contact-icon"><svg viewBox="0 0 12 12"><rect x="3.5" y="1" width="5" height="10" rx="1" fill="#120c0d"/></svg></span>
        555-482-1957
      </li>
      <li class="contact-item">
        <span class="contact-icon"><svg viewBox="0 0 12 12"><rect x="1" y="3" width="10" height="7" fill="#120c0d"/><path d="M1 3 L6 7 L11 3" stroke="#c9a24a" stroke-width="1" fill="none"/></svg></span>
        marty@corvelletrading.example
      </li>
      <li class="contact-item">
        <span class="contact-icon"><svg viewBox="0 0 12 12"><circle cx="6" cy="6" r="4.5" stroke="#120c0d" stroke-width="1.3" fill="none"/><path d="M1.5 6 H10.5 M6 1.5 V10.5" stroke="#120c0d" stroke-width="1"/></svg></span>
        www.corvelletrading.example
      </li>
    </ul>
    <div class="brand">
      <p class="brand-name"><span class="brand-mark"></span>corvelle</p>
      <p class="company">Corvelle Trading/Shipping, LLC.</p>
    </div>
  </section>

  <section class="card card-back" aria-label="Business card back">
    <div class="brand">
      <p class="brand-name"><span class="brand-mark"></span>corvelle</p>
      <p class="company">Corvelle Trading/Shipping, LLC.</p>
      <p class="website">www.corvelletrading.example</p>
    </div>
  </section>
</body>
</html>
```